Oversized Post Card for Busines Owners 1st 2nd and 3rd prizes

Create a professional, fresh and polished oversized post card for law firm specializing in Business Law, Succession Planning, and Employment Law

Use any picture(s) of your choice (mine or ones you recommend), logo, headshot and company info

www.morvenquaylegal.example

Westbrook Office - 4175 Hollister Avenue, Suite 1400, Charlotte, NC 28299
Kestrelmoor Office - 13840 Tamsin Way, Suite 300, Charlotte, NC 28296

Phone (704) 555-0187

Use this card for a Free Consultation

Target Market(s)

Business Owners (of small businesses)

Industry/Entity Type

Business

Font styles to use
Serif
Sans Serif

Requirements
Must have
• Company name, logo and contact info
• Serving business owners with legal guidance
• Business Law, Succession Planning & Wealth Transfers
• www.morvenquaylegal.example
• Westbrook Office - 4175 Hollister Avenue, Suite 1400, Charlotte, NC 28299
• Kestrelmoor Office - 13840 Tamsin Way, Suite 300, Charlotte, NC 28296
• Phone (704) 555-0187
• Use this card for a Free Consultation
Nice to have
• pictures (yours or mine) - you choose; headshot picture

```html
<!DOCTYPE html>
<html lang="en">
<head>
<meta charset="utf-8">
<title>Morven Quay Legal – Oversized Postcard</title>
<link rel="stylesheet" href="https://fonts.googleapis.com/css2?family=Cormorant+Garamond:wght@500;600;700&family=Oswald:wght@600&family=Roboto:wght@500&display=swap">
<style>
  :root{
    --teal:#1b8c97;
    --teal-dark:#136f78;
    --ink:#2e3438;
    --paper:#ffffff;
    --paper-soft:#f1f2f3;
    --backdrop:#dcdddf;
    --photo-dark:#2a2522;
    --photo-warm:#c9a56d;
    --portrait:#d9bf96;
  }
  *{box-sizing:border-box;margin:0;padding:0}
  html,body{width:1200px;height:956px;overflow:hidden}
  body{background:var(--backdrop);position:relative;font-family:"Cormorant Garamond",Georgia,serif;color:var(--ink)}

  .card{position:absolute;top:288px;width:560px;height:380px;background:var(--paper);border-radius:8px;overflow:hidden;box-shadow:0 2px 10px rgba(0,0,0,.12)}
  .card--back{left:30px}
  .card--front{left:610px}

  /* Back */
  .back-panel{position:absolute;left:0;top:0;width:290px;height:380px;background:var(--paper-soft)}
  .back-mailing{position:absolute;left:290px;top:0;width:270px;height:380px;background:var(--paper);border-left:1px solid #e3e4e6}
  .back-swoosh{position:absolute;left:0;top:0;width:290px;height:380px}
  .brand{position:absolute;display:flex;flex-direction:column;align-items:center;text-transform:uppercase;color:var(--teal);font-weight:600;letter-spacing:.08em;line-height:1.05}
  .brand-mark{width:30px;height:30px;border-radius:50%;background:var(--teal);margin-bottom:4px}
  .back-panel .brand{left:0;width:200px;top:8px}
  .brand-name{font-size:17px}
  .brand-sub{font-size:10px;letter-spacing:.14em;margin-top:2px}
  .tagline{position:absolute;left:22px;top:118px;text-transform:uppercase;line-height:.95}
  .tagline-lead{color:var(--teal);font-weight:600;font-size:26px;display:block}
  .tagline-tail{font-size:15px;font-weight:600;display:block;margin-top:2px;padding-left:18px}
  .contact{position:absolute;left:22px;top:196px;font-size:12px;line-height:1.25;text-transform:uppercase;font-weight:600}
  .contact-phone{padding-left:22px;margin-bottom:5px}
  .office{position:relative;padding-left:22px;margin-bottom:5px}
  .office::before{content:"";position:absolute;left:0;top:2px;width:11px;height:26px;background:var(--teal)}
  .office-name{color:var(--teal);font-weight:700;display:block}
  .back-url{position:absolute;left:0;bottom:18px;width:290px;height:30px;background:var(--teal);color:#fff;font-family:Roboto,Arial,sans-serif;font-weight:500;font-size:12px;display:flex;align-items:center;justify-content:center}
  .back-url::before{content:"";position:absolute;left:0;top:-8px;width:290px;height:3px;background:var(--teal)}

  /* Front */
  .front-art{position:absolute;left:0;top:0;width:560px;height:380px}
  .front-photo{fill:url(#photoTone)}
  .portrait{position:absolute;left:322px;top:112px;width:104px;height:104px;border-radius:50%;border:4px solid var(--teal);background:radial-gradient(circle at 50% 40%,var(--portrait),#a78a62 70%,#6b5540);box-shadow:0 0 0 3px #fff}
  .offer{position:absolute;right:16px;top:72px;width:104px;text-align:center;color:#fff;font-family:Oswald,"Arial Narrow",sans-serif;font-weight:600;text-transform:uppercase;line-height:.9}
  .offer-big{display:block;font-size:42px}
  .offer-small{display:block;font-size:13px;letter-spacing:.02em}
  .card--front .brand{left:18px;top:246px;width:150px}
  .services{position:absolute;left:188px;top:236px;text-transform:uppercase;font-weight:700;line-height:1}
  .service{display:block;color:var(--teal);font-size:28px;margin-bottom:2px}
  .service--boxed{display:table;background:var(--teal);color:#fff;padding:0 8px}
  .service--spaced{font-size:21px;letter-spacing:.35em;padding:1px 4px 1px 10px}
  .service--shift{margin-left:18px}
</style>
</head>
<body>

<section class="card card--back" aria-label="Postcard back">
  <div class="back-panel">
    <svg class="back-swoosh" viewBox="0 0 290 380" aria-hidden="true">
      <path d="M0 102 C70 104 150 76 205 72 C240 70 262 86 280 110 C255 90 230 86 200 90 C140 98 70 116 0 112Z" fill="var(--teal)"/>
    </svg>
    <div class="brand">
      <span class="brand-mark"></span>
      <span class="brand-name">Morven Quay</span>
      <span class="brand-sub">Legal, PLLC</span>
    </div>
    <h2 class="tagline">
      <span class="tagline-lead">Serving</span>
      <span class="tagline-lead">Business Owners</span>
      <span class="tagline-tail">With Legal Guidance</span>
    </h2>
    <div class="contact">
      <p class="contact-phone">Phone (704) 555-0187</p>
      <p class="office"><span class="office-name">Westbrook Office</span>4175 Hollister Avenue, Suite 1400,<br>Charlotte, NC 28299</p>
      <p class="office"><span class="office-name">Kestrelmoor Office</span>13840 Tamsin Way, Suite 300,<br>Charlotte, NC 28296</p>
    </div>
    <div class="back-url">www.morvenquaylegal.example</div>
  </div>
  <div class="back-mailing" aria-label="Mailing area"></div>
</section>

<section class="card card--front" aria-label="Postcard front">
  <svg class="front-art" viewBox="0 0 560 380">
    <defs>
      <radialGradient id="photoTone" cx="65%" cy="30%" r="75%">
        <stop offset="0" stop-color="var(--photo-warm)"/>
        <stop offset=".55" stop-color="#5a4a3c"/>
        <stop offset="1" stop-color="var(--photo-dark)"/>
      </radialGradient>
    </defs>
    <path class="front-photo" role="img" aria-label="Photo of small business people standing among large glowing light bulbs" d="M0 0H560V200C470 160 400 175 330 192C230 216 110 222 0 192Z"/>
    <path d="M0 192C110 222 230 216 330 192C400 175 470 160 560 200V210C470 172 400 186 330 202C230 226 110 232 0 204Z" fill="var(--teal)"/>
    <path d="M440 0H560V232C530 212 500 190 470 176C452 120 445 60 440 0Z" fill="var(--teal-dark)" opacity=".92"/>
    <path d="M410 96C450 66 500 56 560 64V76C505 70 455 82 418 108Z" fill="var(--teal)"/>
  </svg>
  <div class="portrait" role="img" aria-label="Headshot of the attorney"></div>
  <p class="offer"><span class="offer-big">Free</span><span class="offer-small">Consultation</span></p>
  <div class="brand">
    <span class="brand-mark"></span>
    <span class="brand-name">Morven Quay</span>
    <span class="brand-sub">Legal, PLLC</span>
  </div>
  <h1 class="services">
    <span class="service service--boxed">Business Law</span>
    <span class="service service--shift">Succession</span>
    <span class="service service--boxed service--spaced service--shift">Planning</span>
    <span class="service">Wealth Transfers</span>
  </h1>
</section>

</body>
</html>
```